SMP by Dana Holloway - Scalp Micropigmentation

I need a wordpress site designed for me, can be based off a theme, I already have a logo and the press site ready to be created, I can provide a login for you. I will be able to update it myself with content I just need the layout done as Im having trouble with it. I want to be able to add pages as needed and have a gallery for my work.

Target Market(s)

customers

Coding

Coded - Design and coding required

Number of Pages Required

5+ page

Font styles to use
Sans Serif

Colors

Designer to choose colors to be used in the design.

Requirements
Must have
• my logo, wordpress, gallery
Should not have
• shopping cart

```html
<!DOCTYPE html>
<html lang="en">
<head>
<meta charset="utf-8">
<title>SMP by Dana Holloway - Scalp Micropigmentation</title>
<link href="https://fonts.googleapis.com/css2?family=Poppins:wght@400;500;600;700&display=swap" rel="stylesheet">
<style>
:root{
  --blue:#2f80c3;
  --blue-deep:#1f5f98;
  --orange:#ee7d22;
  --ink:#2b2b2b;
  --muted:#6d6d6d;
  --light:#f4f4f4;
  --line:#dcdcdc;
  --footer:#15181d;
  --footer-text:#8b9099;
  --white:#ffffff;
}
*{box-sizing:border-box;margin:0;padding:0}
html,body{width:1200px;height:3530px;overflow:hidden}
body{font-family:'Poppins',sans-serif;color:var(--ink);background:var(--white);position:relative}
.wrap{width:936px;margin:0 auto;position:relative}

/* header */
.site-header{height:101px;position:relative}
.brand{position:absolute;left:150px;top:12px;display:flex;align-items:center;gap:10px}
.brand-mark{width:20px;height:20px;background:var(--ink)}
.brand-name{font-size:15px;font-weight:600;color:var(--ink);width:110px;line-height:1.25}
.header-cta{position:absolute;right:132px;top:12px;display:flex;gap:18px}
.pill{height:40px;border-radius:20px;padding:0 34px;display:flex;align-items:center;gap:10px;color:var(--white);font-size:12px;font-weight:600}
.pill-orange{background:var(--orange)}
.pill-blue{background:var(--blue)}
.main-nav{position:absolute;right:132px;top:66px;display:flex;gap:22px;font-size:12.5px;color:var(--ink)}

/* hero */
.hero{height:521px;position:relative;background:linear-gradient(100deg,#3a3430 0%,#6d5a4c 35%,#8a7565 55%,#4a4642 80%,#2c2b2b 100%);text-align:center;color:var(--white)}
.hero::after{content:"";position:absolute;inset:0;background:rgba(0,0,0,.22)}
.hero-inner{position:relative;z-index:1;padding-top:140px}
.hero h1{font-size:33px;font-weight:700;line-height:1.25;text-transform:uppercase;letter-spacing:.5px}
.hero p{font-size:13px;width:560px;margin:14px auto 0;line-height:1.5}
.hero-btns{display:flex;justify-content:center;gap:28px;margin-top:26px}
.btn{display:inline-flex;align-items:center;justify-content:center;height:46px;padding:0 28px;font-size:11.5px;color:var(--white)}
.btn-blue{background:var(--blue);width:250px}
.btn-orange{background:var(--orange);width:126px}
.hero-arrow{position:absolute;top:230px;z-index:1}
.hero-arrow.prev{left:96px}.hero-arrow.next{right:96px}

/* section titles */
.sec-title{text-align:center;font-size:18px;font-weight:600;text-transform:uppercase;letter-spacing:.3px}
.divider{display:block;margin:10px auto 0}

/* welcome */
.welcome{height:258px;padding-top:64px;text-align:center}
.welcome p{width:800px;margin:28px auto 0;font-size:11px;line-height:1.75;color:var(--muted)}

/* fixes */
.fixes{height:788px;background:var(--blue);padding-top:52px;color:var(--white)}
.fix-grid{display:grid;grid-template-columns:repeat(3,294px);gap:27px 27px;margin-top:78px}
.fix-card{background:var(--white);border:3px solid var(--white);height:267px}
.fix-photo{height:207px}
.fix-label{height:54px;display:flex;align-items:center;justify-content:center;font-size:12.5px;font-weight:600;color:var(--ink);text-transform:uppercase}
.tone-a{background:linear-gradient(135deg,#9c7a62,#d9c2ad)}
.tone-b{background:linear-gradient(135deg,#7c6a60,#b8a395)}
.tone-c{background:linear-gradient(135deg,#4e4640,#9a8678)}
.tone-d{background:linear-gradient(135deg,#c9b7a6,#8d705c)}
.tone-e{background:linear-gradient(135deg,#d8d6d3,#55504c)}
.tone-f{background:linear-gradient(135deg,#3c3834,#8b8a86)}

/* testimonials */
.testimonials{height:356px;padding-top:56px;position:relative}
.tst-row{display:flex;justify-content:center;gap:39px;margin-top:56px}
.tst-card{width:243px;height:155px;border:1px solid var(--line);border-radius:14px;position:relative;text-align:center;padding:50px 18px 0}
.avatar{position:absolute;top:-34px;left:50%;margin-left:-32px;width:64px;height:64px;border-radius:50%;border:3px solid var(--white)}
.av-1{background:linear-gradient(#3a5a8a,#28456d)}
.av-2{background:linear-gradient(#4d8a5a,#2e5c3a)}
.av-3{background:linear-gradient(#b89080,#7a5a4e)}
.tst-card p{font-size:9.5px;line-height:1.55;color:var(--muted)}
.tst-name{font-size:11px;margin-top:9px;color:var(--ink)}
.tst-arrow{position:absolute;top:187px;width:26px;height:26px;border-radius:50%;background:#cfcfcf}
.tst-arrow.prev{left:144px}.tst-arrow.next{right:144px}

/* gallery */
.gallery{height:747px;background:var(--light);padding-top:50px}
.filters{display:flex;justify-content:center;gap:24px;margin-top:26px;font-size:11px;color:var(--muted);align-items:center}
.filters .active{background:#6cb6e6;color:var(--white);padding:3px 12px;border-radius:3px}
.gal-grid{display:grid;grid-template-columns:repeat(3,290px);gap:28px 21px;width:912px;margin:24px auto 0}
.gal-item{height:243px}
.g1{background:linear-gradient(135deg,#a8543f,#e4ddd6)}
.g2{background:linear-gradient(135deg,#efe7df,#8a5c48)}
.g3{background:linear-gradient(135deg,#5a4a40,#b6aaa0)}
.g4{background:linear-gradient(90deg,#d9c4b4,#2c3038 50%,#d9c4b4)}
.g5{background:linear-gradient(135deg,#35343a,#a98875)}
.g6{background:linear-gradient(135deg,#c23a2e,#4a3a34)}

/* who we are */
.who{height:304px;position:relative;background:linear-gradient(100deg,#3f7fb8,#2f6fa8 50%,#5a8fbf);text-align:center;color:var(--white);padding-top:70px}
.who h2{font-size:29px;font-weight:600}
.who p{font-size:13px;width:440px;margin:12px auto 0;line-height:1.6}
.who .btn{margin-top:26px;width:240px;height:48px;border-radius:24px;background:var(--orange);font-weight:600;font-size:12.5px;text-transform:uppercase}

/* footer */
.site-footer{height:455px;background:var(--footer);color:var(--footer-text);position:relative}
.foot-cols{position:absolute;top:78px;left:132px;right:132px;height:300px}
.foot-col{position:absolute;top:0}
.foot-col h4{color:var(--white);font-size:16px;font-weight:500;margin-bottom:24px}
.foot-col li{list-style:none;font-size:12px;line-height:30px}
.foot-col li.on{color:var(--white)}
.contact-line{font-size:11.5px;line-height:24px}
.contact-line b{color:var(--white);font-weight:400}
.addr{display:flex;gap:10px;font-size:11.5px;line-height:24px;margin-bottom:18px}
.news p{font-size:11.5px;margin-bottom:18px}
.news-form{display:flex;width:298px;height:40px}
.news-input{flex:1;background:#23272e;display:flex;align-items:center;gap:8px;padding-left:12px;font-size:11px;color:#cfd2d6}
.news-btn{width:100px;background:var(--orange);color:var(--white);font-size:11px;font-weight:600;display:flex;align-items:center;justify-content:center}
.socials{display:flex;gap:10px;margin-top:26px}
.socials span{width:32px;height:32px;border-radius:50%}
.s1{background:#3b5998}.s2{background:#1da1f2}.s3{background:#dd4b39}
.foot-rule{position:absolute;left:132px;right:132px;top:371px;border-top:1px solid #2a2e35}
.copyright{position:absolute;top:396px;width:100%;text-align:center;font-size:11px}
</style>
</head>
<body>

<header class="site-header">
  <div class="brand"><span class="brand-mark"></span><span class="brand-name">SMP by Dana Holloway</span></div>
  <div class="header-cta">
    <span class="pill pill-orange">
      <svg width="12" height="12" viewBox="0 0 12 12"><rect x="1" y="2" width="10" height="9" fill="none" stroke="#fff" stroke-width="1.4"/><line x1="1" y1="5" x2="11" y2="5" stroke="#fff" stroke-width="1.4"/></svg>
      FREE CONSULT</span>
    <span class="pill pill-blue">
      <svg width="12" height="12" viewBox="0 0 24 24"><path d="M6 2l4 5-2 3c1 2 4 5 6 6l3-2 5 4-2 4C10 22 2 14 2 4z" fill="#fff"/></svg>
      555-014-2290</span>
  </div>
  <nav class="main-nav">
    <span>Home</span><span>About Us</span><span>Treatments</span><span>Financing</span><span>Gallery</span><span>Testimonials</span><span>Blog</span><span>FAQ</span><span>Contact Us</span>
  </nav>
</header>

<section class="hero" role="img" aria-label="Photo of an artist holding a hand mirror for a client after a scalp micropigmentation session">
  <svg class="hero-arrow prev" width="16" height="28" viewBox="0 0 16 28"><path d="M14 2L3 14l11 12" fill="none" stroke="#fff" stroke-width="2"/></svg>
  <svg class="hero-arrow next" width="16" height="28" viewBox="0 0 16 28"><path d="M2 2l11 12L2 26" fill="none" stroke="#fff" stroke-width="2"/></svg>
  <div class="hero-inner">
    <h1>Defy hair loss with<br>scalp micropigmentation</h1>
    <p>Dana has a long history of providing fantastic SMP results. Our unique, and most advanced Scalp Pigmentation technique provides you with the best result possible.</p>
    <div class="hero-btns"><span class="btn btn-blue">What is Scalp Micropigmentation?</span><span class="btn btn-orange">Contact us</span></div>
  </div>
</section>

<section class="welcome">
  <h2 class="sec-title">Welcome to SMP</h2>
  <svg class="divider" width="110" height="8" viewBox="0 0 110 8"><line x1="0" y1="4" x2="36" y2="4" stroke="#bbb"/><circle cx="44" cy="4" r="1.6" fill="#555"/><circle cx="50" cy="4" r="1.6" fill="#555"/><circle cx="55" cy="4" r="1.6" fill="#555"/><circle cx="60" cy="4" r="1.6" fill="#555"/><circle cx="66" cy="4" r="1.6" fill="#555"/><line x1="74" y1="4" x2="110" y2="4" stroke="#bbb"/></svg>
  <p>Every client arrives with a story, and each treatment is planned around it. We study your hairline, skin tone and goals before a single dot is placed, so the finished result looks natural up close and from across the room. Sessions are calm, private and paced for comfort, and we stay with you from first consultation to final touch up. Our studio blends careful technique with honest advice, giving you a look you can wear with quiet confidence every day.</p>
</section>

<section class="fixes">
  <h2 class="sec-title">What scalp micropigmentation can fix</h2>
  <svg class="divider" width="110" height="8" viewBox="0 0 110 8"><line x1="0" y1="4" x2="36" y2="4" stroke="#fff" opacity=".6"/><circle cx="44" cy="4" r="1.6" fill="#fff"/><circle cx="50" cy="4" r="1.6" fill="#fff"/><circle cx="55" cy="4" r="1.6" fill="#fff"/><circle cx="60" cy="4" r="1.6" fill="#fff"/><circle cx="66" cy="4" r="1.6" fill="#fff"/><line x1="74" y1="4" x2="110" y2="4" stroke="#fff" opacity=".6"/></svg>
  <div class="wrap fix-grid">
    <div class="fix-card"><div class="fix-photo tone-a" role="img" aria-label="Smiling man with a shaved head after treatment"></div><div class="fix-label">Male pattern baldness</div></div>
    <div class="fix-card"><div class="fix-photo tone-b" role="img" aria-label="Close view of a scalp with alopecia"></div><div class="fix-label">Alopecia</div></div>
    <div class="fix-card"><div class="fix-photo tone-c" role="img" aria-label="Man with a hair transplant looking down"></div><div class="fix-label">Enhancing hair transplants</div></div>
    <div class="fix-card"><div class="fix-photo tone-d" role="img" aria-label="Back of a head with a camouflaged scar"></div><div class="fix-label">Scar camouflage</div></div>
    <div class="fix-card"><div class="fix-photo tone-e" role="img" aria-label="Back of a head with added density"></div><div class="fix-label">Adding density</div></div>
    <div class="fix-card"><div class="fix-photo tone-f" role="img" aria-label="Woman receiving treatment for hair loss"></div><div class="fix-label">Women's hair loss</div></div>
  </div>
</section>

<section class="testimonials">
  <h2 class="sec-title">Client testimonials</h2>
  <span class="tst-arrow prev"></span><span class="tst-arrow next"></span>
  <div class="tst-row">
    <div class="tst-card"><span class="avatar av-1" role="img" aria-label="Client portrait"></span><p>The whole visit felt relaxed and the result looks natural. I finally feel like myself again.</p><div class="tst-name">Marcus Ellery</div></div>
    <div class="tst-card"><span class="avatar av-2" role="img" aria-label="Client portrait"></span><p>Clear advice, steady hands and a hairline that suits my face. Worth every single session.</p><div class="tst-name">Tomas</div></div>
    <div class="tst-card"><span class="avatar av-3" role="img" aria-label="Client portrait"></span><p>My thinning areas blend in now. Friendly studio and careful work from start to finish.</p><div class="tst-name">Priya</div></div>
  </div>
</section>

<section class="gallery">
  <h2 class="sec-title">Gallery</h2>
  <div class="filters"><span class="active">All</span><span>Bold, Shaved Look</span><span>Scalp Scar</span><span>Thinning Hair</span><span>Female SMP</span></div>
  <div class="gal-grid">
    <div class="gal-item g1" role="img" aria-label="Artist working on a client's scalp"></div>
    <div class="gal-item g2" role="img" aria-label="Technician marking a hairline"></div>
    <div class="gal-item g3" role="img" aria-label="Client checking the result in a mirror"></div>
    <div class="gal-item g4" role="img" aria-label="Before and after comparison of a client"></div>
    <div class="gal-item g5" role="img" aria-label="Client reclined during a session"></div>
    <div class="gal-item g6" role="img" aria-label="Artist applying pigment close up"></div>
  </div>
</section>

<section class="who" role="img" aria-label="Blue tinted photo of a man on a city street">
  <h2>Who We Are</h2>
  <p>Learn how the fusion of passion, experience, &amp; understanding created the World Leaders in Scalp Micropigmentation.</p>
  <span class="btn">Make an appointment</span>
</section>

<footer class="site-footer">
  <div class="foot-cols">
    <div class="foot-col" style="left:0;width:250px">
      <h4>Contact Information</h4>
      <div class="addr">
        <svg width="12" height="16" viewBox="0 0 12 16" style="margin-top:4px;flex:none"><path d="M6 0a6 6 0 0 0-6 6c0 4.5 6 10 6 10s6-5.5 6-10a6 6 0 0 0-6-6zm0 8.5A2.5 2.5 0 1 1 6 3.5a2.5 2.5 0 0 1 0 5z" fill="var(--orange)"/></svg>
        <span>Studio Row, Eastfield, Block 2<br>48 Harbor Lane, Suite 5</span>
      </div>
      <div class="contact-line"><b>Email:</b> hello@smpdana.example</div>
      <div class="contact-line"><b>Phone:</b> 5550 142 290</div>
    </div>
    <div class="foot-col" style="left:275px">
      <h4>Navigation</h4>
      <ul><li>Home</li><li>About us</li><li>Services</li><li>pages</li><li>Blog</li><li class="on">Careers</li><li>Contact</li></ul>
    </div>
    <div class="foot-col" style="left:434px">
      <h4>Services</h4>
      <ul><li>Hairline</li><li>Pattern baldness</li><li>scar camouflage</li></ul>
    </div>
    <div class="foot-col news" style="left:641px">
      <h4>Newsletter</h4>
      <p>Enter your email &amp; subscribing newsletter</p>
      <div class="news-form">
        <span class="news-input"><svg width="14" height="10" viewBox="0 0 14 10"><rect x=".5" y=".5" width="13" height="9" fill="none" stroke="var(--orange)"/><path d="M.5 .5L7 6l6.5-5.5" fill="none" stroke="var(--orange)"/></svg>Email address</span>
        <span class="news-btn">SUBSCRIBE</span>
      </div>
      <div class="socials"><span class="s1"></span><span class="s2"></span><span class="s3"></span></div>
    </div>
  </div>
  <div class="foot-rule"></div>
  <div class="copyright">2017 &copy; smpdana.example. All rights reserved</div>
</footer>

</body>
</html>
```